Rate Card

We wish to update our rate card flyer.I have uploaded a copy of our current version, which has a black background but we want to redesign this with a cleaner and fresh look with a white background. Our new logo also needs to be used.

The stats on the why choose us need to be updated also.

- 8,000+ sales agreed
- £2.1bn sales value
- £41m savings
- 97.5% recommended
- 5,000 client testimonials

We would like a new look to this double sided flyer.

This is an urgent requirement so anyone that posts a design we like quickly will more than likely get this order!

```html
<!DOCTYPE html>
<html lang="en">
<head>
<meta charset="utf-8">
<title>Keyline Homes – Fee Menu</title>
<link href="https://fonts.googleapis.com/css2?family=Arvo:wght@400;700&family=Open+Sans:wght@400;600&display=swap" rel="stylesheet">
<style>
  :root {
    --pink: #e8408f;
    --cyan: #6dd6f7;
    --orange: #fbab62;
    --green: #b6e06a;
    --blue: #27aee3;
    --ink: #2b2b2b;
    --brand-grey: #5a5a5a;
    --panel-line: #a7a7a7;
    --badge-green: #3d8c6a;
    --badge-purple: #6a2f7d;
    --badge-blue: #2d6fa3;
    --badge-red: #b8202a;
    --badge-dark: #333;
    --badge-review: #7b3a8c;
  }
  * { box-sizing: border-box; margin: 0; padding: 0; }
  html, body { width: 844px; height: 1200px; overflow: hidden; background: #fff; }
  body { position: relative; font-family: "Arvo", serif; color: var(--ink); }

  .side { position: absolute; left: 15px; width: 813px; height: 580px; border: 2px solid var(--panel-line); }
  .side--front { top: 15px; }
  .side--back { top: 605px; }
  .abs { position: absolute; }

  /* front */
  .fee-title { left: 0; width: 100%; top: 66px; text-align: center; font-weight: 700; font-size: 50px; color: var(--pink); }

  .fee-table { left: 33px; top: 146px; width: 748px; border-collapse: collapse; font-size: 18px; font-weight: 400; }
  .fee-table td, .fee-table th { border: 2px solid var(--pink); height: 54px; padding: 0 9px; text-align: left; font-weight: 400; }
  .fee-table th:not(.col-label) { padding-left: 20px; }
  .fee-table td.fill { padding-left: 20px; }
  .fee-table .col-label { width: 176px; }
  .fee-table .col-up { width: 146px; }
  .fee-table .col-comp { width: 210px; }
  .fee-table .total { font-weight: 700; }
  .vat { font-size: 14px; }
  .row-cyan td.fill { background: var(--cyan); }
  .row-orange td.fill { background: var(--orange); }
  .row-green td.fill { background: var(--green); }
  .fee-table td.beat { font-size: 14px; padding-left: 20px; }
  .beat sup { font-size: 9px; }
  .footnote { right: 47px; top: 372px; font-family: "Open Sans", sans-serif; font-size: 10px; }

  .advertised { left: 51px; top: 469px; font-size: 17px; color: var(--blue); }
  .listing-badge { top: 512px; height: 26px; border-radius: 4px; }
  .listing-badge--a { left: 50px; width: 124px; background: var(--badge-green); }
  .listing-badge--b { left: 203px; width: 100px; background: var(--badge-purple); }
  .listing-badge--c { left: 333px; width: 115px; background: var(--badge-blue); }

  .brand { left: 545px; top: 488px; display: flex; align-items: center; gap: 12px; }
  .brand-mark { width: 44px; height: 44px; background: var(--pink); }
  .brand-text { font-family: "Arvo", serif; font-weight: 400; color: var(--brand-grey); }
  .brand-name { font-size: 24px; line-height: 1.1; }
  .brand-tag { font-size: 13px; margin-top: 3px; }

  /* back */
  .why-title { left: 49px; top: 50px; font-weight: 700; font-size: 46px; color: var(--pink); }
  .featured { left: 597px; top: 38px; font-size: 16px; color: var(--blue); }
  .press-badge { border-radius: 2px; }
  .press-badge--a { left: 598px; top: 67px; width: 60px; height: 40px; background: var(--blue); }
  .press-badge--b { left: 662px; top: 67px; width: 60px; height: 40px; background: var(--badge-red); }
  .press-badge--c { left: 598px; top: 119px; width: 124px; height: 29px; background: var(--badge-dark); }

  .section-head { font-weight: 700; font-size: 19px; color: var(--pink); line-height: 26px; }
  .stats-head { left: 49px; top: 153px; }
  .service-head { left: 407px; top: 179px; }

  .ticks { list-style: none; font-size: 14.5px; line-height: 24.6px; }
  .ticks li { position: relative; padding-left: 13px; white-space: nowrap; }
  .ticks li::before { content: ""; position: absolute; left: 1px; top: 8px; border-left: 5px solid var(--pink); border-top: 4px solid transparent; border-bottom: 4px solid transparent; }
  .stats-list { left: 49px; top: 216px; width: 360px; }
  .service-list { left: 407px; top: 216px; width: 380px; }
  .ticks .wrap { line-height: 20px; margin-top: 2px; }

  .review-badge { left: 64px; top: 448px; width: 210px; height: 42px; border-radius: 8px; background: var(--badge-review); }

  .contact { left: 556px; top: 408px; display: flex; gap: 12px; font-family: "Open Sans", sans-serif; font-size: 12px; line-height: 13px; }
  .contact-mark { width: 36px; height: 36px; background: var(--pink); margin-top: 2px; }
  .contact-brand { font-style: normal; }
  .contact-brand .accent { color: var(--pink); }
  .contact-phone { margin-top: 22px; }
  .contact-web { color: var(--pink); margin-top: 2px; }
</style>
</head>
<body>

<section class="side side--front">
  <h1 class="abs fee-title">fee menu</h1>

  <table class="abs fee-table">
    <tr>
      <th class="col-label"></th>
      <th class="col-up">upfront</th>
      <th class="col-comp">completion</th>
      <th class="total">total</th>
    </tr>
    <tr class="row-cyan">
      <td>no commission</td>
      <td class="fill">£495+<span class="vat">VAT</span></td>
      <td class="fill">£0</td>
      <td class="fill total">£495+<span class="vat">VAT</span></td>
    </tr>
    <tr class="row-orange">
      <td>commission</td>
      <td class="fill">£195+<span class="vat">VAT</span></td>
      <td class="fill">£795+<span class="vat">VAT</span></td>
      <td class="fill">£990+<span class="vat">VAT</span></td>
    </tr>
    <tr class="row-green">
      <td>no sale- no fee</td>
      <td class="fill">£0</td>
      <td class="fill beat">we’ll beat any quote<sup>*</sup></td>
      <td class="fill beat">we’ll beat any quote<sup>*</sup></td>
    </tr>
  </table>
  <p class="abs footnote"><sup>*</sup>subject to a minimum fee of £1000</p>

  <p class="abs advertised">Your property advertised on</p>
  <div class="abs listing-badge listing-badge--a" role="img" aria-label="Property portal badge"></div>
  <div class="abs listing-badge listing-badge--b" role="img" aria-label="Property portal badge"></div>
  <div class="abs listing-badge listing-badge--c" role="img" aria-label="Property portal badge"></div>

  <div class="abs brand">
    <div class="brand-mark"></div>
    <div class="brand-text">
      <div class="brand-name">Keyline Homes</div>
      <div class="brand-tag">smart selling, made simple</div>
    </div>
  </div>
</section>

<section class="side side--back">
  <h2 class="abs why-title">why choose us?</h2>

  <p class="abs featured">As Featured on</p>
  <div class="abs press-badge press-badge--a" role="img" aria-label="Broadcaster badge"></div>
  <div class="abs press-badge press-badge--b" role="img" aria-label="Broadcaster badge"></div>
  <div class="abs press-badge press-badge--c" role="img" aria-label="Broadcaster badge"></div>

  <h3 class="abs section-head stats-head">Strength in numbers<br>since our launch in 2003</h3>
  <ul class="abs ticks stats-list">
    <li>8,000+ sales agreed</li>
    <li>£2.1bn sales value</li>
    <li>£41m savings</li>
    <li>£4,500 average fee SAVING vs high street</li>
    <li>97.5% recommended</li>
    <li>5,000 client testimonials</li>
    <li>9/10 average client rating</li>
    <li class="wrap">Rated no. 2 estate agent in the UK<br>by the independent Verdict Index</li>
  </ul>

  <h3 class="abs section-head service-head">Customer Service</h3>
  <ul class="abs ticks service-list">
    <li>Personal account manager with direct dial</li>
    <li>Online account to track your progress</li>
    <li>All staff are PEAA qualified</li>
    <li>Weekly activity reports keep you in the loop</li>
    <li>Live web chat facility after hours</li>
    <li class="wrap">Full personal estate agency service from<br>instruction to completion</li>
  </ul>

  <div class="abs review-badge" role="img" aria-label="Review site rating badge"></div>

  <div class="abs contact">
    <div class="contact-mark"></div>
    <address class="contact-brand">
      <div><span class="accent">Keyline</span> Homes</div>
      <div>Estate Offices</div>
      <div>Ashby Mill Barn</div>
      <div>Ashby Mill Lane</div>
      <div>Ashby Vale</div>
      <div>Essex&nbsp; CM9 4XQ</div>
      <div class="contact-phone">T 0845 276 4410</div>
      <div class="contact-web">www.keylinehomes.co.uk</div>
    </address>
  </div>
</section>

</body>
</html>
```